Business card for Crestline Bathrooms

Please design a business card for our bathroom renovation business. You can use my existing logo, but if you have an idea to modernize it, I would like to see it. Please see attached files first. I would like to use the blue and the orange theme. I like the concept of using the shower head in the logo. Please find following a design (or two) that I have been trying to create with my limited resources. That design was for a sign, but I was going to adopt it and use it as a business card as well. I like the concept of the water splash but I don’t think it “flows” nicely together with the logo. Another thought is that maybe creating the logo out of water splash could work and have a dramatic effect (like the water text and the butterfly picture attached with similar background instead of white). If the above doesn’t work I would like to see a modern simplified design. One of the attached files named as the unwanted business card has all the details that I want included in the business card. Please note that it is two sided.
Updates

I am very thankful for the designs that I have received, but they are very similar and only a couple of attempts to do something with the water splash as per my original brief. Modernizing the logo and having it made out of out of water splash with the orange as color accent could work and have a dramatic effect (like the water text and the butterfly picture attached with similar background instead of white). Please do not use the butterfly itself! This is just an example that images can be created out of water splash.

Contact Information for Business Card

all the details are on the unwonted business card file included

Colors
3176b5

Requirements
Nice to have
• Copied from the brief:
• ... maybe creating the logo out of water splash could work and have a dramatic effect (like the water text and the butterfly picture attached with similar background instead of white). Please do not use the butterfly itself!
Should not have
• I am getting designs with a butterfly. The butterfly picture was an example of creating something from a water splash. The butterfly itself has no association with anything other than the concept of creating a logo out of water splash. Sorry, I thought I was clear in the brief.

```html
<!DOCTYPE html>
<html lang="en">
<head>
<meta charset="utf-8">
<title>Crestline Bathrooms – Business Card</title>
<link href="https://fonts.googleapis.com/css2?family=Roboto:wght@400;500&family=Roboto+Condensed:wght@500&display=swap" rel="stylesheet">
<style>
  :root {
    --navy: #0b416b;
    --coral: #e9796c;
    --paper: #f3f3f2;
    --backdrop: #dedede;
    --white: #ffffff;
  }
  * { margin: 0; padding: 0; box-sizing: border-box; }
  html, body {
    width: 1200px; height: 960px; overflow: hidden;
    background: var(--backdrop);
    font-family: "Roboto", Arial, sans-serif;
  }
  .card {
    position: absolute;
    width: 602px; height: 343px;
    border-radius: 18px;
    overflow: hidden;
  }
  .card--front { left: 314px; top: 113px; background: var(--paper); }
  .card--back  { left: 311px; top: 472px; width: 600px; height: 342px; background: var(--navy); }

  .front-wave { position: absolute; inset: 0; width: 100%; height: 100%; }

  .brand {
    position: absolute;
    display: flex; align-items: center; gap: 10px;
    font-family: "Roboto", Arial, sans-serif;
    font-weight: 500;
    line-height: 1.05;
  }
  .brand__dot { width: 16px; height: 16px; border-radius: 50%; background: var(--coral); flex: none; }
  .brand__name { font-size: 34px; letter-spacing: 0.5px; }
  .brand__name span { display: block; }
  .brand--front { left: 56px; top: 128px; color: var(--navy); }
  .brand--back { left: 0; right: 0; top: 110px; justify-content: center; color: var(--white); }

  .contact {
    position: absolute; right: 26px; top: 158px;
    color: var(--white); text-align: right;
    font-size: 14.5px; line-height: 19.5px;
  }
  .contact__name {
    font-family: "Roboto Condensed", Arial, sans-serif;
    font-weight: 500; font-size: 21px; letter-spacing: 0.3px;
    margin-bottom: 6px;
  }
  .contact__address { margin-bottom: 8px; margin-right: 0; }
  .contact__line { display: flex; justify-content: flex-end; align-items: center; gap: 10px; }
  .contact__icon { width: 14px; height: 14px; flex: none; }

  .services {
    position: absolute; left: 0; right: 0; top: 187px;
    color: var(--white); text-align: center;
    font-size: 14.5px; line-height: 18.5px;
  }
  .memberships {
    position: absolute; left: 0; right: 0; top: 276px;
    display: flex; justify-content: center; align-items: center; gap: 18px;
  }
  .badge { background: var(--white); }
  .badge--round { width: 32px; height: 32px; border-radius: 8px; }
  .badge--wide { width: 116px; height: 26px; border-radius: 3px; }
  .memberships__divider { width: 1px; height: 34px; background: var(--white); }
</style>
</head>
<body>

<section class="card card--front" aria-label="Card front">
  <svg class="front-wave" viewBox="0 0 602 343" preserveAspectRatio="none" aria-hidden="true">
    <path fill="var(--coral)" d="M48 343 C220 318 300 230 352 150 C398 80 440 8 532 0 L602 0 L602 343 Z"/>
    <path fill="var(--navy)" d="M66 343 C236 322 318 236 370 156 C414 88 456 10 552 0 L602 0 L602 343 Z"/>
  </svg>

  <div class="brand brand--front">
    <div class="brand__dot"></div>
    <div class="brand__name"><span>Crestline</span><span>Bathrooms</span></div>
  </div>

  <div class="contact">
    <div class="contact__name">DANIEL MARKOVIC</div>
    <div class="contact__address">PO Box 418<br>Kelsworth 2743</div>
    <div class="contact__line">0400 555 218
      <svg class="contact__icon" viewBox="0 0 16 16" aria-hidden="true"><path fill="var(--white)" d="M3.5 1 6 3.6 4.6 5.5c.8 1.9 2.2 3.3 4.1 4.1L10.6 8.2 13.2 10.6 12 14c-5.6-.4-9.7-4.4-10.2-10z"/></svg>
    </div>
    <div class="contact__line">5550 2194
      <svg class="contact__icon" viewBox="0 0 16 16" aria-hidden="true"><rect x="4" y="1" width="8" height="14" rx="1.5" fill="none" stroke="var(--white)" stroke-width="1.6"/><circle cx="8" cy="12.3" r="0.9" fill="var(--white)"/></svg>
    </div>
    <div class="contact__line">daniel@crestlinebathrooms.com.au
      <svg class="contact__icon" viewBox="0 0 16 16" aria-hidden="true"><rect x="1.5" y="3.5" width="13" height="9" fill="var(--white)"/><path d="M1.5 3.5 8 9l6.5-5.5" fill="none" stroke="var(--navy)" stroke-width="1.2"/></svg>
    </div>
    <div class="contact__line">crestlinebathrooms.com.au
      <svg class="contact__icon" viewBox="0 0 16 16" aria-hidden="true"><circle cx="8" cy="8" r="6.5" fill="var(--white)"/><path d="M5 5c2 0 2 2 4 2s1 3-1 3-1 2-2 3M10 3c0 2 2 1 3 3" fill="none" stroke="var(--navy)" stroke-width="1.2"/></svg>
    </div>
  </div>
</section>

<section class="card card--back" aria-label="Card back">
  <div class="brand brand--back">
    <div class="brand__dot"></div>
    <div class="brand__name"><span>Crestline</span><span>Bathrooms</span></div>
  </div>

  <div class="services">
    <p>Complete Bathroom Renovations &amp; Remodelling</p>
    <p>Highly Skilled &amp; Qualified Tradespeople</p>
    <p>Professional Service From Concept To Completion</p>
    <p>All Work Guaranteed</p>
  </div>

  <div class="memberships">
    <div class="badge badge--round" role="img" aria-label="Trade association membership badge"></div>
    <div class="memberships__divider"></div>
    <div class="badge badge--wide" role="img" aria-label="Builders association membership badge"></div>
  </div>
</section>

</body>
</html>
```